DESIGN A ALL CROWD PULLER A CATCHY NIGHT CLUBB FLYER.Ngoma is simple a drum...Include A beautiful African girl with a A-FRO AND A DRUM

Target Market(s)

NIGHT CLUBB GOERS

Industry/Entity Type

Crowd

Requirements
Must have
• launching:TV-VELDA RUSHO

HOUSE PARTY!

Bored & feeling like grooving to Funkhouse.Dance. Dubstep.Electro.Afro beat.
R n B,Hip Hop.Dancehall. Reggae.Raggaeton. Zouk.Live bands & Poerty

Velda Rusho is the place to be

Friday the 16th Jan. 2015 9pm-3am
& every second Friday of the month

@ TOLM Prins Halvard gate 42,5032 Bergen

AGE:18+ KR 100

New Year, New Klubb,New City vibes & sounds!!

For more information visit our site
www.lorenvisuals.org fb-veldarusho

DRINKS & FOOD SAVED ON CASH ONLY!!
Nice to have
• Add a African girl with a Afro and DRUM

```html
<!DOCTYPE html>
<html lang="en">
<head>
<meta charset="utf-8">
<title>TV-Velda Rusho – House Party</title>
<link href="https://fonts.googleapis.com/css2?family=Monoton&family=Nunito:wght@700;800;900&family=Fredoka:wght@600;700&family=Oswald:wght@500;600&display=swap" rel="stylesheet">
<style>
  :root{
    --bg-deep:#3a0a6e;
    --bg-mid:#7a1bb8;
    --bg-hot:#d23cc8;
    --lavender:#c9a6ff;
    --lavender-edge:#3b0f6a;
    --ribbon:#c3161d;
    --ribbon-dark:#7e0b10;
    --neon-red:#e0202a;
    --gold:#f2c646;
    --white:#ffffff;
    --black-band:#141018;
    --badge:#c8e83a;
    --badge-text:#c0147a;
  }
  *{margin:0;padding:0;box-sizing:border-box}
  html,body{width:801px;height:1200px;overflow:hidden;background:var(--bg-deep)}
  .flyer{
    position:relative;width:801px;height:1200px;overflow:hidden;
    background:
      radial-gradient(ellipse 60% 40% at 50% 28%, rgba(255,150,240,.55), transparent 70%),
      radial-gradient(ellipse 70% 30% at 30% 75%, rgba(255,80,220,.45), transparent 70%),
      linear-gradient(180deg,#5a1596 0%,var(--bg-mid) 35%,var(--bg-hot) 60%,var(--bg-mid) 80%,var(--bg-deep) 100%);
    font-family:"Nunito",sans-serif;color:var(--white);
  }
  .hero-art{
    position:absolute;left:120px;top:150px;width:600px;height:560px;
    border-radius:46% 46% 38% 38%;
    background:
      radial-gradient(ellipse 28% 40% at 52% 62%, #ff5fc8 0%, #e83aa8 60%, transparent 100%),
      radial-gradient(ellipse 22% 22% at 50% 30%, #2a1030 0%, #3a1a44 60%, transparent 100%),
      radial-gradient(circle at 40% 55%, #e9e4f4 0%, #b9a8d8 30%, #8c5cc8 55%, rgba(140,40,190,.5) 72%, transparent 82%);
  }
  .launch-frame{position:absolute;left:90px;top:38px;width:615px;height:122px}
  .launch-text{
    position:absolute;left:90px;top:68px;width:615px;text-align:center;
    font-weight:800;font-size:29px;line-height:38px;letter-spacing:1px;
    text-shadow:0 0 6px rgba(255,255,255,.6);
  }
  .genres{
    position:absolute;font-family:"Fredoka",sans-serif;font-weight:600;
    color:var(--lavender);font-size:23px;letter-spacing:1.5px;
    -webkit-text-stroke:1px var(--lavender-edge);
  }
  .genres-left{left:23px;top:298px;line-height:27px}
  .genres-right{right:40px;top:396px;text-align:right;line-height:31px}
  .new-badge{position:absolute;left:44px;top:606px;width:150px;height:110px}
  .presents{position:absolute;left:213px;top:640px;width:412px;height:46px}
  .presents-text{
    position:absolute;left:213px;top:646px;width:412px;text-align:center;
    font-family:"Oswald",sans-serif;font-weight:600;font-size:23px;letter-spacing:1px;
  }
  .title-house{
    position:absolute;left:0;top:694px;width:801px;text-align:center;
    font-family:"Monoton",sans-serif;font-size:106px;line-height:122px;
    color:#f4c8ff;text-shadow:0 0 10px #ff4fd8,0 0 22px #a12bff;letter-spacing:2px;
  }
  .title-party{
    position:absolute;left:0;top:810px;width:801px;text-align:center;
    font-family:"Fredoka",sans-serif;font-weight:700;font-size:82px;line-height:92px;
    color:var(--white);text-shadow:0 3px 0 #5a8bd8,0 0 14px #6fd1ff;
  }
  .cash-band{
    position:absolute;left:0;top:914px;width:801px;height:56px;
    background:linear-gradient(180deg,var(--neon-red),var(--ribbon-dark));
    text-align:center;font-weight:900;font-size:21px;line-height:25px;padding-top:3px;
  }
  .date-band{position:absolute;left:0;top:988px;width:801px;height:58px}
  .date-text{
    position:absolute;left:0;top:994px;width:801px;text-align:center;
    font-weight:700;font-size:36px;line-height:46px;
  }
  .date-text small{font-size:24px}
  .recurring{
    position:absolute;left:0;top:1050px;width:801px;text-align:center;
    font-weight:900;font-size:26px;line-height:32px;color:var(--gold);letter-spacing:.5px;
    -webkit-text-stroke:.6px #6a2a00;
  }
  .dates{position:absolute;left:0;top:1083px;width:801px;text-align:center;font-weight:800;font-size:18px;line-height:24px}
  .details{
    position:absolute;left:0;top:1108px;width:801px;text-align:center;
    font-weight:700;font-size:13px;line-height:15.5px;
  }
  .web{position:absolute;left:0;top:1174px;width:801px;text-align:center;font-weight:900;font-size:15px;line-height:20px}
</style>
</head>
<body>
<main class="flyer">
  <div class="hero-art" role="img" aria-label="Illustration of a dancing woman in a pink top in front of a mirrored disco ball and speakers"></div>

  <svg class="launch-frame" viewBox="0 0 615 122" aria-hidden="true">
    <defs>
      <linearGradient id="neon" x1="0" x2="1">
        <stop offset="0" stop-color="#ffd21e"/><stop offset=".5" stop-color="#ff7a1a"/><stop offset="1" stop-color="#ff2a2a"/>
      </linearGradient>
    </defs>
    <rect x="6" y="6" width="603" height="110" rx="24" fill="rgba(20,6,30,.88)" stroke="url(#neon)" stroke-width="8"/>
    <rect x="14" y="14" width="587" height="94" rx="18" fill="none" stroke="#ffb84a" stroke-width="2" opacity=".7"/>
  </svg>
  <div class="launch-text">LAUNCHING<br>TV-VELDA RUSHO</div>

  <div class="genres genres-left">FUNKYHOUSE<br>DANCEELECTRO<br>AFRO BEAT</div>
  <div class="genres genres-right">R N B.HIP HOP.<br>DANCEHALL.<br>REGGAE.<br>RAGGAETON.<br>ZOUK.<br>LIVE BANDS &amp; POERTY</div>

  <svg class="presents" viewBox="0 0 412 46" aria-hidden="true">
    <polygon points="0,5 412,0 400,23 412,46 0,41" fill="var(--ribbon)"/>
    <rect x="0" y="41" width="412" height="4" fill="var(--ribbon-dark)"/>
  </svg>
  <div class="presents-text">M.O.V.E &amp; TOLM PRESENTS</div>

  <svg class="new-badge" viewBox="0 0 150 110" aria-hidden="true">
    <circle cx="64" cy="55" r="50" fill="var(--badge)"/>
    <polygon points="4,64 136,34 142,56 10,86" fill="var(--badge)" stroke="#8fae14" stroke-width="2"/>
    <text x="70" y="68" text-anchor="middle" transform="rotate(-14 70 62)" font-family="Fredoka, sans-serif" font-weight="700" font-size="38" fill="var(--badge-text)">new</text>
  </svg>

  <div class="title-house">HOUSE</div>
  <div class="title-party">Party</div>

  <div class="cash-band">DRINKS &amp; FOOD SAVED ON CASH ONLY!!<br>BORED &amp; FEELING LIKE GROOVING TO FUNKHOUSE</div>

  <svg class="date-band" viewBox="0 0 801 58" aria-hidden="true">
    <polygon points="40,1 761,1 790,29 761,57 40,57 11,29" fill="var(--black-band)" stroke="#ffffff" stroke-width="2"/>
  </svg>
  <div class="date-text">FRIDAY <small>the</small> 16<small>th</small> Jan. 2015/9pm-3am</div>

  <div class="recurring">EVERY SECOND FRIDAY OF THE MONTH</div>
  <div class="dates">13th Feb, 13th Mar, 17th Apr, 22th Mai, 12th Juni, 2015</div>
  <div class="details">Velda Rusho is the place to be<br>@ TOLM Prins Halvard gate 42,5032 Bergen<br>AGE:18+ KR 100<br>New Year, New Klubb,New City vibes &amp; sounds!!</div>
  <div class="web">WWW.LORENVISUALS.ORG &nbsp; fb-veldarusho</div>
</main>
</body>
</html>
```